-Photo booth rental Web Design Project

Our business is a small photo booth rental service serving the capital region and surrounding areas. The photo booth is a portable booth that fits up to 10 guest. I am looking for a website that will have social media capabilities and also private log ins for clients to view their photo albums online after their event. We provide full service photo booth rentals for all types of parties. I am looking for something fun and unique but also professional and I am also looking to maybe somehow incorporate the age of the photo booth which was invented in 1888. I do not have the photos of our photo booth available because we are just starting up and I wanted to get everything together first but I will provide stock photo booth pictures .Thank you for your patience i know it wont be an easy task with out those things. I added a word document describing information i will need on our website, i am looking for a home page, contact us and book an event page, online gallery page, and pricing. If you need any more information please feel free to contact me. Thanks for your help and I look forward to working with you.

Target Market(s)

For everyone from brides to be for their weddings or private parties, corporate parties, school dances, charity events, community events ect

Industry/Entity Type

Business

Requirements
Nice to have
• social media sharing

```html
<!DOCTYPE html>
<html lang="en">
<head>
<meta charset="utf-8">
<title>Giggle Frames Photo Booth – Pricing</title>
<link rel="stylesheet" href="https://fonts.googleapis.com/css2?family=EB+Garamond:wght@400;500&family=Parisienne&display=swap">
<style>
  :root {
    --page-yellow: #ebd63a;
    --page-glow: #f7ec8e;
    --panel: #d3c430;
    --ribbon: #a8924a;
    --ribbon-fold: #6e5d25;
    --tab-orange: #fb9c0a;
    --corner-orange: #f79c12;
    --ink-dark: #2e2116;
    --text-light: #ffffff;
  }
  * { box-sizing: border-box; margin: 0; padding: 0; }
  html, body { width: 1200px; height: 1200px; overflow: hidden; }
  body {
    position: relative;
    background: radial-gradient(ellipse 300px 180px at 600px 70px, var(--page-glow), var(--page-yellow) 100%), var(--page-yellow);
    font-family: "EB Garamond", Georgia, serif;
    color: var(--text-light);
  }
  .corner { position: absolute; }
  .corner-top { left: 0; top: 0; }
  .corner-bottom { right: 0; bottom: 0; }

  .brand {
    position: absolute; left: 0; width: 1200px; top: 42px;
    display: flex; justify-content: center; align-items: center; gap: 14px;
  }
  .brand-name {
    font-family: "EB Garamond", Georgia, serif;
    font-weight: 500; font-size: 44px; line-height: 1; color: var(--ink-dark);
  }
  .brand-mark { width: 26px; height: 26px; border-radius: 50%; background: var(--ink-dark); }

  .nav-tab {
    position: absolute; width: 188px; height: 52px;
    background: var(--tab-orange);
    display: flex; align-items: center; justify-content: center;
    padding-right: 14px;
    font-family: "Parisienne", cursive; font-size: 22px; color: var(--text-light);
    white-space: nowrap;
    transform: rotate(-9deg);
    box-shadow: 3px 6px 8px rgba(120, 90, 0, 0.35);
    text-decoration: none;
  }

  .page-title {
    position: absolute; left: 0; width: 1200px; top: 262px; text-align: center;
    font-family: "Parisienne", cursive; font-size: 62px; color: var(--text-light);
    transform: rotate(-8deg);
  }

  .package {
    position: absolute; top: 380px; width: 325px; height: 542px;
    background: var(--panel);
    box-shadow: 6px 8px 14px rgba(150, 120, 0, 0.25);
  }
  .package-name { margin-top: 18px; text-align: center; font-size: 40px; font-weight: 400; line-height: 1.1; }
  .package-tier { margin-top: 24px; text-align: center; font-size: 21px; line-height: 30px; }
  .package-details {
    margin: 0 28px; font-size: 21px; line-height: 30px;
    text-align: justify; text-align-last: center; hyphens: manual;
  }
  .price {
    position: absolute; left: -16px; top: 465px; width: 244px; height: 53px;
    background: var(--ribbon); font-size: 46px; line-height: 53px;
    text-align: right; padding-right: 18px;
    box-shadow: 2px 5px 8px rgba(90, 70, 0, 0.3);
  }
  .price::before {
    content: ""; position: absolute; left: 0; top: -6px;
    border-style: solid; border-width: 0 16px 6px 0;
    border-color: transparent var(--ribbon-fold) transparent transparent;
  }

  .addons {
    position: absolute; left: 63px; top: 973px; width: 1074px; height: 160px;
    background: var(--panel); text-align: center;
    box-shadow: 6px 8px 14px rgba(150, 120, 0, 0.25);
    font-size: 33px; line-height: 38px; padding-top: 14px;
  }
  .deposit {
    display: inline-block; margin-top: 10px; padding: 0 12px;
    background: var(--ribbon); line-height: 42px;
  }
</style>
</head>
<body>
  <svg class="corner corner-top" width="190" height="42" viewBox="0 0 190 42" aria-hidden="true">
    <polygon points="0,0 185,0 0,40" fill="var(--corner-orange)"/>
  </svg>
  <svg class="corner corner-bottom" width="200" height="42" viewBox="0 0 200 42" aria-hidden="true">
    <polygon points="200,0 200,42 10,42" fill="var(--corner-orange)"/>
  </svg>

  <header class="brand">
    <span class="brand-name">Giggle Frames photo booth</span>
    <span class="brand-mark"></span>
  </header>

  <nav>
    <a class="nav-tab" style="left:164px;top:180px;">Home</a>
    <a class="nav-tab" style="left:337px;top:170px;">Pricing</a>
    <a class="nav-tab" style="left:513px;top:168px;">Contact Us</a>
    <a class="nav-tab" style="left:689px;top:170px;">Book An Event</a>
    <a class="nav-tab" style="left:862px;top:166px;">Client Log In</a>
  </nav>

  <h1 class="page-title">Pricing</h1>

  <section class="package" style="left:63px;">
    <h2 class="package-name">Package 1</h2>
    <p class="package-tier">Standard- includes:</p>
    <p class="package-details">3 hours of service, set up &amp; re&shy;moval, professional &amp; friendly booth attendant, dvd or usb flash drive of picture, guest&shy;book, unlimited prints, online gallery, digital backdrop.</p>
    <div class="price">$675</div>
  </section>

  <section class="package" style="left:433px;">
    <h2 class="package-name">Package 2</h2>
    <p class="package-tier">Ultimate- includes:</p>
    <p class="package-details">4 hours of service, set up &amp; re&shy;moval, professional &amp; friendly booth attendant, dvd or usb flash drive of picture gallery, guestbook, unlimited prints, custom backdrop, video mes&shy;saging, props package, online gallery, instant social media up&shy;loads, digital backdrop.</p>
    <div class="price">$850</div>
  </section>

  <section class="package" style="left:812px;">
    <h2 class="package-name">Package 3</h2>
    <p class="package-tier">Extreme- includes:</p>
    <p class="package-details">5 hours of service, set up &amp; re&shy;moval, professional &amp; friendly booth attendant, dvd or usb flash drive of picture gallery, guestbook, unlimited prints, custom backdrop, video mes&shy;saging, props package, online gallery, red carpet event (velvet rope and carpet) , instant social media uploads, digital back&shy;drop.</p>
    <div class="price">$975</div>
  </section>

  <section class="addons">
    <p>Add on’s:</p>
    <p>Magnet photo strip frames, stand up acrylic photo strip frames,</p>
    <p class="deposit">ONLY $100 deposit</p>
  </section>
</body>
</html>
```